Specialized Personal Trainer Needs a Business Card Design

I need a business card design for my personal training business called Tall Oak Fitness. I have my Human Kinetics degree in Exercise Science from the Halvern Ridge University as well as an extra certification from NBEP (National Board of Exercise Practice). I work as a Cardiac Rehab Exercise Specialist and personal trainer giving specialized exercise prescriptions to those that have different heart conditions as well as work with the general population in weight loss, strength and conditioning, getting/staying fit.
Updates

I decided that I wanted a logo (as I did not have one before I submitted my project for a business card) so I am submitting a project to get a logo done and then I will decide on a business card, hopefully being able to use one of the designs already submitted.  My apologies for doing this backwards.  I am new to this so I appreciate your patience.

Thank you.

Hi, I have just created a project for a logo design (I realized I needed a logo and I should've done that first..oops!), please feel free to participate.  Once I receive a logo I like I will finalize my business card project and hopefully incorporate it into one of your business card designs. 

Thank you!

Target Market(s)

Business professionals

Industry/Entity Type

Personal Trainer

Requirements
Must have
• My name with my info:
Celia R. Dunhill (BHK)
NBEP Certified Clinical Exercise Specialist & Personal Trainer
celia.dunhill@talloakfitness.example
Cell: 604-358-4170

Please make it double sided.
Nice to have
• An image that represents cardiac and general fitness training.

```html
<!DOCTYPE html>
<html lang="en">
<head>
<meta charset="utf-8">
<title>Tall Oak Fitness – Stationery</title>
<link rel="stylesheet" href="https://fonts.googleapis.com/css2?family=Roboto+Condensed:wght@400;700&display=swap">
<style>
  :root{
    --bg:#1e2021;
    --paper:#f4f4f4;
    --red:#e01f26;
    --red-deep:#9c1519;
    --maroon:#5e1414;
    --edge:#3d3d3d;
    --ink:#2a2a2a;
    --logo:#7a1a1a;
    --white:#ffffff;
  }
  *{box-sizing:border-box;margin:0;padding:0}
  html,body{width:1200px;height:1197px;overflow:hidden;background:var(--bg)}
  body{position:relative;font-family:"Roboto Condensed",Arial,sans-serif;color:var(--ink)}

  .card{position:absolute;width:540px;height:309px;overflow:hidden}
  .card svg.face{position:absolute;inset:0;width:100%;height:100%}
  .card--front{left:40px;top:50px}
  .card--back{left:620px;top:50px}

  .logo{position:absolute;font-weight:700;text-transform:uppercase;color:var(--logo);
        letter-spacing:.5px;white-space:nowrap;transform-origin:left bottom;line-height:1}
  .card .logo{left:30px;top:62px;font-size:34px;transform:rotate(-6deg)}
  .card--back .logo{top:78px}

  .holder{position:absolute;left:26px;top:140px;width:230px;transform:rotate(-4deg);text-align:center}
  .holder__name{font-weight:700;font-size:19px;padding-bottom:4px;border-bottom:2px solid var(--ink);text-align:left}
  .holder__role{font-size:13px;line-height:1.25;margin-top:6px}

  .contact{position:absolute;color:var(--white);transform:rotate(-4deg);transform-origin:left top}
  .card .contact{left:272px;top:130px;font-size:15px}
  .contact__row{display:flex;align-items:center;gap:12px;margin-bottom:8px;white-space:nowrap}
  .contact__icon{display:block;flex:none}
  .contact__text{display:block;flex:none}

  .envelope{position:absolute;left:40px;top:470px;width:640px;height:330px}
  .envelope svg.sheet{position:absolute;inset:0;width:100%;height:100%}
  .envelope .logo{left:72px;top:98px;font-size:18px;transform:rotate(-5deg)}
  .envelope .contact{left:502px;top:150px;font-size:7px}
  .envelope .contact__row{gap:4px;margin-bottom:3px}

  .letterhead{position:absolute;left:730px;top:400px;width:430px;height:557px;overflow:hidden}
  .letterhead svg.sheet{position:absolute;inset:0;width:100%;height:100%}
  .letterhead .contact{left:284px;top:468px;font-size:8px}
  .letterhead .contact__row{gap:5px;margin-bottom:4px}
</style>
</head>
<body>

<svg width="0" height="0" style="position:absolute" aria-hidden="true">
  <defs>
    <linearGradient id="paperFront" x1="0" y1="0" x2="1" y2="1">
      <stop offset="0" stop-color="#ffffff"/><stop offset="1" stop-color="#dcdcdc"/>
    </linearGradient>
    <linearGradient id="redPanel" x1="0" y1="1" x2="1" y2="0">
      <stop offset="0" stop-color="#a8161b"/><stop offset=".5" stop-color="#e01f26"/><stop offset="1" stop-color="#e42129"/>
    </linearGradient>
    <linearGradient id="band" x1="0" y1="0" x2="1" y2="0">
      <stop offset="0" stop-color="#5e1414"/><stop offset=".6" stop-color="#c41c22"/><stop offset="1" stop-color="#e01f26"/>
    </linearGradient>
    <linearGradient id="envPaper" x1="0" y1="0" x2="0" y2="1">
      <stop offset="0" stop-color="#f6f6f6"/><stop offset="1" stop-color="#e2e2e2"/>
    </linearGradient>
    <radialGradient id="sheetShade" cx=".45" cy=".4" r=".8">
      <stop offset="0" stop-color="#f7f7f7"/><stop offset="1" stop-color="#dcdcdc"/>
    </radialGradient>
  </defs>
</svg>

<!-- Business card front -->
<section class="card card--front" aria-label="Business card, front">
  <svg class="face" viewBox="0 0 540 309" aria-hidden="true">
    <rect width="540" height="309" fill="url(#redPanel)"/>
    <polygon points="0,262 285,240 540,230 540,309 0,309" fill="url(#band)"/>
    <polygon points="0,0 540,0 540,38 275,100 285,240 0,262" fill="url(#paperFront)"/>
    <polyline points="540,44 280,104 290,243 0,266" fill="none" stroke="var(--edge)" stroke-width="7"/>
    <line x1="540" y1="36" x2="276" y2="97" stroke="#9a9a9a" stroke-width="3"/>
    <rect x="310" y="60" width="190" height="235" fill="#b8181e" opacity=".45" role="img" aria-label="Silhouette of a person walking on a treadmill"/>
  </svg>
  <div class="logo">Tall Oak Fitness</div>
  <div class="holder">
    <div class="holder__name">Celia R. Dunhill (BHK)</div>
    <div class="holder__role">NBEP Certified Clinical Exercise<br>Specialist &amp; Personal Trainer</div>
  </div>
  <div class="contact">
    <div class="contact__row">
      <svg class="contact__icon" width="24" height="24" viewBox="0 0 24 24" aria-hidden="true"><rect x="1" y="1" width="22" height="22" rx="6" fill="#fff" stroke="#3d3d3d" stroke-width="2"/><rect x="8" y="5" width="8" height="14" rx="1.5" fill="#e01f26"/><rect x="9.5" y="7" width="5" height="5" fill="#fff"/></svg>
      <span class="contact__text">Cell: 604-358-4170</span>
    </div>
    <div class="contact__row">
      <svg class="contact__icon" width="24" height="24" viewBox="0 0 24 24" aria-hidden="true"><rect x="1" y="1" width="22" height="22" rx="6" fill="#fff" stroke="#3d3d3d" stroke-width="2"/><rect x="5" y="7.5" width="14" height="9" rx="1" fill="#e01f26"/><polyline points="5.5,8 12,13 18.5,8" fill="none" stroke="#fff" stroke-width="1.3"/></svg>
      <span class="contact__text">celia.dunhill@talloakfitness.example</span>
    </div>
  </div>
</section>

<!-- Business card back -->
<section class="card card--back" aria-label="Business card, back">
  <svg class="face" viewBox="0 0 540 309" aria-hidden="true">
    <rect width="540" height="309" fill="url(#redPanel)"/>
    <polygon points="0,262 285,240 540,230 540,309 0,309" fill="url(#band)"/>
    <polygon points="0,0 540,0 540,38 275,100 285,240 0,262" fill="url(#paperFront)"/>
    <polyline points="540,44 280,104 290,243 0,266" fill="none" stroke="var(--edge)" stroke-width="7"/>
    <line x1="540" y1="36" x2="276" y2="97" stroke="#9a9a9a" stroke-width="3"/>
    <rect x="310" y="60" width="190" height="235" fill="#b8181e" opacity=".45" role="img" aria-label="Silhouette of a person walking on a treadmill"/>
  </svg>
  <div class="logo">Tall Oak Fitness</div>
</section>

<!-- Envelope -->
<section class="envelope" aria-label="Envelope">
  <svg class="sheet" viewBox="0 0 640 330" aria-hidden="true">
    <path d="M40,0 H600 Q620,0 620,20 V40 H640 V170 Q640,190 620,195 V330 H20 V195 Q0,190 0,170 V40 H20 V20 Q20,0 40,0 Z" fill="url(#envPaper)" stroke="#cfcfcf"/>
    <line x1="20" y1="42" x2="620" y2="42" stroke="#b5b5b5" stroke-dasharray="4 3"/>
    <line x1="20" y1="42" x2="20" y2="190" stroke="#b5b5b5" stroke-dasharray="4 3"/>
    <line x1="620" y1="42" x2="620" y2="190" stroke="#b5b5b5" stroke-dasharray="4 3"/>
    <rect x="140" y="20" width="120" height="150" fill="#d6d6d6" opacity=".7" role="img" aria-label="Faint silhouette of a person walking on a treadmill"/>
    <polygon points="495,140 620,118 620,190 500,194" fill="#e01f26"/>
    <polyline points="620,120 493,142 498,196" fill="none" stroke="var(--edge)" stroke-width="3"/>
    <rect x="575" y="122" width="25" height="66" fill="#b8181e" opacity=".5" role="img" aria-label="Small silhouette of a person on a treadmill"/>
    <polygon points="20,196 620,188 620,194 20,202" fill="url(#band)"/>
  </svg>
  <div class="logo">Tall Oak Fitness</div>
  <div class="contact">
    <div class="contact__row"><svg class="contact__icon" width="8" height="8" viewBox="0 0 24 24" aria-hidden="true"><rect x="1" y="1" width="22" height="22" rx="6" fill="#fff"/><rect x="8" y="5" width="8" height="14" rx="1.5" fill="#e01f26"/></svg><span class="contact__text">Cell: 604-358-4170</span></div>
    <div class="contact__row"><svg class="contact__icon" width="8" height="8" viewBox="0 0 24 24" aria-hidden="true"><rect x="1" y="1" width="22" height="22" rx="6" fill="#fff"/><rect x="5" y="7.5" width="14" height="9" fill="#e01f26"/></svg><span class="contact__text">celia.dunhill@talloakfitness.example</span></div>
  </div>
</section>

<!-- Letterhead -->
<section class="letterhead" aria-label="Letterhead">
  <svg class="sheet" viewBox="0 0 430 557" aria-hidden="true">
    <rect width="430" height="557" fill="url(#sheetShade)"/>
    <rect x="80" y="40" width="290" height="380" fill="#d3d3d3" opacity=".55" role="img" aria-label="Large faint silhouette of a person walking on a treadmill"/>
    <polygon points="275,458 430,428 430,557 0,557 0,540 280,530" fill="#e01f26"/>
    <polygon points="0,540 280,530 430,526 430,557 0,557" fill="url(#band)"/>
    <polyline points="430,430 272,461 278,533 0,543" fill="none" stroke="var(--edge)" stroke-width="4"/>
    <line x1="430" y1="424" x2="272" y2="455" stroke="#9a9a9a" stroke-width="2"/>
    <rect x="385" y="432" width="35" height="92" fill="#b8181e" opacity=".5" role="img" aria-label="Small silhouette of a person on a treadmill"/>
  </svg>
  <div class="contact">
    <div class="contact__row"><svg class="contact__icon" width="10" height="10" viewBox="0 0 24 24" aria-hidden="true"><rect x="1" y="1" width="22" height="22" rx="6" fill="#fff"/><rect x="8" y="5" width="8" height="14" rx="1.5" fill="#e01f26"/></svg><span class="contact__text">Cell: 604-358-4170</span></div>
    <div class="contact__row"><svg class="contact__icon" width="10" height="10" viewBox="0 0 24 24" aria-hidden="true"><rect x="1" y="1" width="22" height="22" rx="6" fill="#fff"/><rect x="5" y="7.5" width="14" height="9" fill="#e01f26"/></svg><span class="contact__text">celia.dunhill@talloakfitness.example</span></div>
  </div>
</section>

</body>
</html>
```